Business Card Design Project - 2 sided

We need a business card design for a card having one business on each side (ie. two businesses on one card). Would like a design that incorporates logo, tagline and normal fields (name, position, address, phone).

Would also like an allowance for small font text along the bottom (text to be determined, but less than 50 characters).

NB. Attached logo for Verbal Bridgeworks has two variations - either can be used.

www.verbalbridgeworks.com / www.kelpora.com

```html
<!DOCTYPE html>
<html lang="en">
<head>
<meta charset="utf-8">
<title>Two-sided business card – Verbal Bridgeworks / Kelpora</title>
<link rel="stylesheet" href="https://fonts.googleapis.com/css2?family=Cinzel:wght@400;600&family=Arimo:wght@400;700&display=swap">
<style>
  :root {
    --stage-light: #4a4a4a;
    --stage-dark: #2a2a2a;
    --card-white: #fdfdfd;
    --card-edge: #d9d9d9;
    --green: #8cc43f;
    --green-light: #a6d65a;
    --blue: #1a9ad6;
    --blue-light: #3bb3e6;
    --navy: #2e3a78;
    --text: #2b2b2b;
    --icon: #555555;
    --divider: #8a8a8a;
  }
  * { margin: 0; padding: 0; box-sizing: border-box; }
  html, body { width: 1200px; height: 1062px; overflow: hidden; }
  body {
    position: relative;
    background: radial-gradient(ellipse 70% 60% at 50% 40%, var(--stage-light), var(--stage-dark));
    font-family: "Arimo", Arial, sans-serif;
  }
  .card {
    position: absolute;
    top: 413px;
    width: 522px;
    height: 294px;
    background: radial-gradient(ellipse 75% 80% at 50% 45%, var(--card-white) 45%, var(--card-edge));
    box-shadow: 0 2px 6px rgba(0,0,0,0.35);
    overflow: hidden;
  }
  .card--bridgeworks { left: 34px; }
  .card--kelpora { left: 643px; }
  .card__band { position: absolute; left: 0; top: 115px; width: 522px; height: 49px; }
  .brand {
    position: absolute;
    font-family: "Arimo", Arial, sans-serif;
    font-weight: 400;
    color: var(--text);
    white-space: nowrap;
  }
  .brand--bridgeworks {
    left: 16px; top: 70px;
    font-size: 22px;
    letter-spacing: 0.3px;
  }
  .brand--kelpora {
    left: 16px; top: 34px;
    font-size: 34px;
  }
  .person {
    position: absolute;
    left: 26px; top: 115px;
    height: 49px;
    display: flex;
    align-items: center;
    color: #ffffff;
  }
  .person__name {
    font-family: "Cinzel", serif;
    font-size: 22px;
    letter-spacing: 0.5px;
    padding-right: 10px;
    border-right: 1px solid rgba(255,255,255,0.85);
    line-height: 32px;
  }
  .person__title {
    font-family: "Cinzel", serif;
    font-size: 8.5px;
    letter-spacing: 0.6px;
    padding-left: 8px;
  }
  .address {
    position: absolute;
    left: 62px; top: 228px;
    display: flex;
    align-items: center;
    gap: 7px;
    font-size: 12.5px;
    color: var(--text);
  }
  .contacts {
    position: absolute;
    left: 288px; top: 206px;
    height: 58px;
    padding-left: 14px;
    border-left: 1.5px solid var(--divider);
    list-style: none;
    font-size: 12.5px;
    color: var(--text);
  }
  .contacts li { display: flex; align-items: center; gap: 8px; height: 15px; margin-top: 2px; }
  .contacts svg, .address svg { fill: var(--icon); flex: none; }
</style>
</head>
<body>

<section class="card card--bridgeworks" aria-label="Verbal Bridgeworks side">
  <div class="brand brand--bridgeworks">Verbal Bridgeworks</div>
  <svg class="card__band" viewBox="0 0 522 49" aria-hidden="true">
    <defs>
      <linearGradient id="greenBand" x1="0" y1="0" x2="0" y2="1">
        <stop offset="0" stop-color="var(--green-light)"/>
        <stop offset="1" stop-color="var(--green)"/>
      </linearGradient>
    </defs>
    <polygon points="0,0 459,0 449,49 0,49" fill="url(#greenBand)"/>
    <polygon points="466,0 522,0 522,49 456,49" fill="var(--navy)"/>
  </svg>
  <div class="person">
    <span class="person__name">Martin Hale</span>
    <span class="person__title">Managing Director</span>
  </div>
  <p class="address">
    <svg width="15" height="13" viewBox="0 0 15 13"><path d="M7.5 0 15 6.5h-2V13H9V9H6v4H2V6.5H0z"/></svg>
    48, Elm Court, New York, USA
  </p>
  <ul class="contacts">
    <li><svg width="8" height="11" viewBox="0 0 8 11"><path d="M1 0h6a1 1 0 0 1 1 1v9a1 1 0 0 1-1 1H1a1 1 0 0 1-1-1V1a1 1 0 0 1 1-1zm0 1.5v7h6v-7z"/></svg>216-555-0147</li>
    <li><svg width="11" height="8" viewBox="0 0 11 8"><path d="M0 0h11v8H0zm1 1v.3l4.5 3 4.5-3V1zm0 1.5V7h9V2.5L5.5 5.5z"/></svg>martin@verbalbridgeworks.com</li>
    <li><svg width="11" height="11" viewBox="0 0 11 11"><circle cx="5.5" cy="5.5" r="5.5"/></svg>www.verbalbridgeworks.com</li>
  </ul>
</section>

<section class="card card--kelpora" aria-label="Kelpora side">
  <div class="brand brand--kelpora">Kelpora</div>
  <svg class="card__band" viewBox="0 0 522 49" aria-hidden="true">
    <defs>
      <linearGradient id="blueBand" x1="0" y1="0" x2="0" y2="1">
        <stop offset="0" stop-color="var(--blue-light)"/>
        <stop offset="1" stop-color="var(--blue)"/>
      </linearGradient>
    </defs>
    <polygon points="0,0 459,0 449,49 0,49" fill="url(#blueBand)"/>
    <polygon points="466,0 522,0 522,49 456,49" fill="var(--green)"/>
  </svg>
  <div class="person">
    <span class="person__name">Martin Hale</span>
    <span class="person__title">Managing Director</span>
  </div>
  <p class="address">
    <svg width="15" height="13" viewBox="0 0 15 13"><path d="M7.5 0 15 6.5h-2V13H9V9H6v4H2V6.5H0z"/></svg>
    48, Elm Court, New York, USA
  </p>
  <ul class="contacts">
    <li><svg width="8" height="11" viewBox="0 0 8 11"><path d="M1 0h6a1 1 0 0 1 1 1v9a1 1 0 0 1-1 1H1a1 1 0 0 1-1-1V1a1 1 0 0 1 1-1zm0 1.5v7h6v-7z"/></svg>216-555-0147</li>
    <li><svg width="11" height="8" viewBox="0 0 11 8"><path d="M0 0h11v8H0zm1 1v.3l4.5 3 4.5-3V1zm0 1.5V7h9V2.5L5.5 5.5z"/></svg>martin@verbalbridgeworks.com</li>
    <li><svg width="11" height="11" viewBox="0 0 11 11"><circle cx="5.5" cy="5.5" r="5.5"/></svg>www.verbalbridgeworks.com</li>
  </ul>
</section>

</body>
</html>
```